Stationery Design for Meadowline Ledger

We need new stationery designed with our new logo (attached). Need at minimum business cards (with space for headshots), cd sleeve, envelopes, letterhead and two distintively different folders.

One element design only will automatically be eliminated.

Industry/Entity Type

Accountant

Font styles to use
Sans Serif

Colors

Designer to choose colors to be used in the design.

Requirements
Must have
• business cards (with space for headshots),
• cd sleeve,
• envelopes (Size 10 and flat letter size - must comply with US Postal Standards)
• letterhead
• two distinctively different folders (one for IRS Resolution and one for Business Services)
Nice to have
• a third folder design for taxes
• Multiple Cd designs - with "password = last four of last name+last 5 of social
Should not have
• a lot of black

```html
<!DOCTYPE html>
<html lang="en">
<head>
<meta charset="utf-8">
<title>Meadowline Ledger — Stationery Set</title>
<link rel="stylesheet" href="https://fonts.googleapis.com/css2?family=Montserrat:wght@400;500;600&family=Libre+Baskerville&display=swap">
<style>
  :root {
    --backdrop: #6b6b6b;
    --gold: #d3ad3b;
    --ink: #2a1d1f;
    --black: #000000;
    --paper: #ffffff;
    --text: #3a3a3a;
    --faint: #f3f3f3;
  }
  * { margin: 0; padding: 0; box-sizing: border-box; }
  html, body { width: 1200px; height: 1200px; overflow: hidden; background: var(--backdrop); }
  .stage {
    position: relative; width: 1500px; height: 1500px;
    transform: scale(0.8); transform-origin: 0 0;
    font-family: "Montserrat", sans-serif; color: var(--text);
  }
  .shapes { position: absolute; left: 0; top: 0; width: 1500px; height: 1500px; }
  .label {
    position: absolute; color: var(--paper); font-weight: 600; font-size: 12px;
    letter-spacing: .2px; transform: translateX(-50%); white-space: nowrap;
  }
  .brand { position: absolute; display: flex; align-items: center; gap: 5px; white-space: nowrap; }
  .brand__dot { width: 1.1em; height: 1.1em; border-radius: 50%; background: var(--gold); flex: none; }
  .brand__text { display: flex; flex-direction: column; line-height: 1; }
  .brand__name { color: var(--gold); font-weight: 600; text-transform: uppercase; }
  .brand__tag { color: var(--ink); font-size: .38em; letter-spacing: .4px; margin-top: 2px; text-transform: uppercase; }
  .contact { position: absolute; font-size: 6px; line-height: 12px; white-space: nowrap; color: var(--text); }
  .contact span { margin-right: 10px; }
  .contact span::before { content: ""; display: inline-block; width: 4px; height: 4px; border-radius: 50%; background: var(--gold); margin-right: 3px; vertical-align: middle; }
  .contact--compact { font-size: 5.5px; }
  .contact--compact span { margin-right: 7px; }
  .card-name { position: absolute; font-size: 8px; color: var(--text); }
  .thanks-title {
    position: absolute; left: 1284px; top: 262px; width: 165px; text-align: center;
    font-family: "Libre Baskerville", serif; font-size: 11px; line-height: 16px; color: var(--text);
  }
  .thanks-title__brand { font-family: "Montserrat", sans-serif; color: var(--gold); font-weight: 600; font-size: 6px; }
  .thanks-body {
    position: absolute; left: 1302px; top: 326px; width: 130px; text-align: center;
    font-size: 4.6px; line-height: 9.8px; color: var(--text);
  }
  .folder-brand { position: absolute; left: 1070px; top: 840px; width: 314px; display: flex; flex-direction: column; align-items: center; }
  .folder-brand__dot { width: 70px; height: 70px; border-radius: 50%; background: var(--gold); margin-bottom: 18px; }
  .folder-brand__name { color: var(--gold); font-weight: 600; font-size: 19px; text-transform: uppercase; }
  .folder-brand__tag { color: var(--ink); font-size: 7.5px; letter-spacing: .5px; margin-top: 2px; }
</style>
</head>
<body>
<div class="stage">

  <svg class="shapes" viewBox="0 0 1500 1500" xmlns="http://www.w3.org/2000/svg">
    <defs>
      <clipPath id="disc"><circle cx="949" cy="1324" r="137"/></clipPath>
      <linearGradient id="photoTone" x1="0" y1="0" x2="1" y2="1">
        <stop offset="0" stop-color="#c9c4bd"/><stop offset="1" stop-color="#2f3540"/>
      </linearGradient>
      <linearGradient id="deskTone" x1="0" y1="0" x2="1" y2="1">
        <stop offset="0" stop-color="#f7f7f7"/><stop offset=".5" stop-color="#eeeeee"/><stop offset="1" stop-color="#fbfbfb"/>
      </linearGradient>
    </defs>

    <g class="business-card-front">
      <rect x="50" y="115" width="224" height="128" fill="var(--paper)"/>
      <polygon points="145,115 195,115 170,143" fill="var(--ink)"/>
      <polygon points="205,115 274,115 274,243 255,243 172,150" fill="var(--gold)"/>
      <rect x="200" y="117" width="74" height="126" fill="url(#photoTone)" role="img" aria-label="Headshot of the account manager"/>
    </g>
    <rect class="business-card-back" x="51" y="268" width="224" height="128" fill="var(--paper)"/>

    <g class="letterhead">
      <rect x="343" y="115" width="304" height="393" fill="var(--paper)"/>
      <polygon points="558,115 606,115 582,143" fill="var(--ink)"/>
      <polygon points="612,115 647,115 647,225 588,148" fill="var(--gold)"/>
    </g>

    <g class="envelope-letter">
      <polygon points="737,92 1013,92 1021,115 729,115" fill="var(--gold)"/>
      <rect x="729" y="115" width="292" height="412" fill="var(--paper)"/>
      <polygon points="906,115 970,115 938,153" fill="var(--ink)"/>
      <polygon points="978,115 1021,115 1021,255 943,160" fill="var(--gold)"/>
    </g>

    <g class="thank-you-card">
      <rect x="1097" y="224" width="165" height="259" fill="var(--paper)"/>
      <polygon points="1143,290 1262,290 1262,483 1165,483 1097,410 1097,335" fill="var(--gold)"/>
      <polygon points="1097,410 1155,483 1097,483" fill="var(--black)"/>
      <rect x="1118" y="312" width="128" height="130" fill="var(--gold)" role="img" aria-label="Hand lettered thank you message"/>
      <rect x="1284" y="224" width="165" height="259" fill="var(--paper)"/>
    </g>

    <g class="envelope-no10">
      <rect x="146" y="618" width="365" height="190" fill="var(--paper)"/>
      <polygon points="511,618 533,626 533,800 511,808" fill="var(--gold)"/>
      <polygon points="390,618 446,618 418,652" fill="var(--ink)"/>
      <polygon points="457,618 511,618 511,765 425,658" fill="var(--gold)"/>
    </g>

    <g class="folder-business">
      <rect x="755" y="599" width="315" height="422" fill="var(--gold)"/>
      <rect x="1070" y="599" width="314" height="422" fill="url(#deskTone)" role="img" aria-label="Faint photo of charts and a calculator on a desk"/>
      <rect x="1070" y="599" width="314" height="422" fill="none" stroke="#dddddd"/>
      <polygon points="736,1040 755,1021 755,1160 736,1145" fill="var(--black)"/>
      <polygon points="755,1021 1070,1021 1053,1160 755,1160" fill="var(--black)"/>
    </g>

    <g class="folder-resolution">
      <rect x="74" y="911" width="293" height="395" fill="var(--paper)"/>
      <rect x="367" y="911" width="294" height="395" fill="var(--paper)"/>
      <line x1="367" y1="911" x2="367" y2="1306" stroke="#cfcfcf"/>
      <polygon points="385,995 430,960 570,1140 540,1175" fill="var(--faint)"/>
      <polygon points="390,911 418,911 452,958 440,975" fill="var(--gold)"/>
      <polygon points="425,911 545,911 485,985" fill="var(--black)"/>
      <polygon points="558,911 661,911 661,1195 493,1003" fill="var(--gold)"/>
      <polygon points="485,1050 505,1025 661,1200 661,1270" fill="var(--black)"/>
      <polygon points="55,1325 74,1306 74,1436 55,1420" fill="var(--black)"/>
      <polygon points="74,1306 367,1306 350,1436 74,1436" fill="var(--gold)"/>
    </g>

    <g class="cd-label">
      <circle cx="949" cy="1324" r="137" fill="var(--paper)"/>
      <g clip-path="url(#disc)">
        <polygon points="915,1180 1030,1180 975,1265" fill="var(--ink)"/>
        <polygon points="1037,1200 1100,1200 1100,1385 1075,1378 1000,1255" fill="var(--gold)"/>
      </g>
      <circle cx="949" cy="1324" r="42" fill="var(--backdrop)"/>
    </g>

    <g class="cd-sleeve">
      <rect x="1139" y="1169" width="273" height="273" fill="var(--paper)"/>
      <polygon points="1240,1169 1330,1169 1285,1225" fill="var(--ink)"/>
      <polygon points="1345,1169 1412,1169 1412,1375 1290,1236" fill="var(--gold)"/>
      <circle cx="1412" cy="1305" r="22" fill="var(--backdrop)"/>
    </g>
  </svg>

  <div class="label" style="left:148px; top:73px;">BUSINESS CARD</div>
  <div class="label" style="left:490px; top:73px;">LETTERHEAD</div>
  <div class="label" style="left:864px; top:73px;">ENVELOPE 1</div>
  <div class="label" style="left:1270px; top:167px;">THANK YOU CARD</div>
  <div class="label" style="left:335px; top:588px;">ENVELOPE 2</div>
  <div class="label" style="left:1075px; top:556px;">FOLDER 1</div>
  <div class="label" style="left:367px; top:876px;">FOLDER 2</div>
  <div class="label" style="left:1272px; top:1126px;">CD SLEEVES</div>
  <div class="label" style="left:771px; top:1400px;">CD LABEL</div>

  <!-- Business card front -->
  <div class="brand" style="left:62px; top:165px; font-size:7.5px;">
    <span class="brand__dot"></span>
    <span class="brand__text"><span class="brand__name">Meadowline Ledger</span><span class="brand__tag">Accounting &amp; Tax Solutions</span></span>
  </div>
  <div class="card-name" style="left:88px; top:193px;">Daniel Harlow</div>
  <div class="contact" style="left:88px; top:203px; line-height:8px; font-size:5.5px;">
    <span>555-214-0187</span><br><span>daniel.harlow@mail.com</span><br><span>www.meadowlineledger.com</span>
  </div>

  <!-- Business card back -->
  <div class="brand" style="left:100px; top:321px; font-size:10px;">
    <span class="brand__dot"></span>
    <span class="brand__text"><span class="brand__name">Meadowline Ledger</span><span class="brand__tag">Accounting &amp; Tax Solutions</span></span>
  </div>
  <div class="contact" style="left:51px; top:369px; width:224px; text-align:center; font-size:5px;">42 Fernbrook Rd, Marlow, Ohio, 43015</div>

  <!-- Letterhead -->
  <div class="brand" style="left:367px; top:150px; font-size:14px;">
    <span class="brand__dot"></span>
    <span class="brand__text"><span class="brand__name">Meadowline Ledger</span><span class="brand__tag">Accounting &amp; Tax Solutions</span></span>
  </div>
  <div class="contact" style="left:365px; top:469px;">
    <span>555-214-0187</span><span>info@meadowlineledger.com</span><span>www.meadowlineledger.com</span><br><span>42 Fernbrook Rd, Marlow, Ohio, 43015</span>
  </div>

  <!-- Envelope 1 -->
  <div class="brand" style="left:750px; top:150px; font-size:12px;">
    <span class="brand__dot"></span>
    <span class="brand__text"><span class="brand__name">Meadowline Ledger</span><span class="brand__tag">Accounting &amp; Tax Solutions</span></span>
  </div>
  <div class="contact" style="left:750px; top:485px;">
    <span>555-214-0187</span><span>info@meadowlineledger.com</span><span>www.meadowlineledger.com</span><br><span>42 Fernbrook Rd, Marlow, Ohio, 43015</span>
  </div>

  <!-- Thank you card -->
  <div class="brand" style="left:1110px; top:251px; font-size:8.5px;">
    <span class="brand__dot"></span>
    <span class="brand__text"><span class="brand__name">Meadowline Ledger</span><span class="brand__tag">Accounting &amp; Tax Solutions</span></span>
  </div>
  <div class="thanks-title">With sincere<br>appreciation from all of<br>us at <span class="thanks-title__brand">MEADOWLINE LEDGER</span></div>
  <p class="thanks-body">Thank you for trusting our team with your books and filings this season. We value every question you bring and every deadline we meet together. Our door stays open all year for planning, reviews and quiet advice. We look forward to helping your finances grow steady and clear in the years ahead.</p>

  <!-- Envelope 2 -->
  <div class="brand" style="left:169px; top:648px; font-size:13px;">
    <span class="brand__dot"></span>
    <span class="brand__text"><span class="brand__name">Meadowline Ledger</span><span class="brand__tag">Accounting &amp; Tax Solutions</span></span>
  </div>
  <div class="contact" style="left:169px; top:766px;">
    <span>555-214-0187</span><span>info@meadowlineledger.com</span><span>www.meadowlineledger.com</span><br><span>42 Fernbrook Rd, Marlow, Ohio, 43015</span>
  </div>

  <!-- Folder 1 -->
  <div class="brand" style="left:783px; top:948px; font-size:9px;">
    <span class="brand__dot" style="background:var(--ink);"></span>
    <span class="brand__text"><span class="brand__name" style="color:var(--ink);">Meadowline Ledger</span><span class="brand__tag">Accounting &amp; Tax Solutions</span></span>
  </div>
  <div class="contact contact--compact" style="left:781px; top:977px; color:var(--paper);">
    <span>555-214-0187</span><span>info@meadowlineledger.com</span><span>www.meadowlineledger.com</span><br><span>42 Fernbrook Rd, Marlow, Ohio, 43015</span>
  </div>
  <div class="folder-brand">
    <span class="folder-brand__dot"></span>
    <span class="folder-brand__name">Meadowline Ledger</span>
    <span class="folder-brand__tag">ACCOUNTING &amp; TAX SOLUTIONS</span>
  </div>

  <!-- Folder 2 -->
  <div class="brand" style="left:99px; top:1238px; font-size:9px;">
    <span class="brand__dot"></span>
    <span class="brand__text"><span class="brand__name">Meadowline Ledger</span><span class="brand__tag">Accounting &amp; Tax Solutions</span></span>
  </div>
  <div class="contact contact--compact" style="left:97px; top:1265px;">
    <span>555-214-0187</span><span>info@meadowlineledger.com</span><span>www.meadowlineledger.com</span><br><span>42 Fernbrook Rd, Marlow, Ohio, 43015</span>
  </div>
  <div class="brand" style="left:397px; top:1233px; font-size:15px;">
    <span class="brand__dot"></span>
    <span class="brand__text"><span class="brand__name">Meadowline Ledger</span><span class="brand__tag">Accounting &amp; Tax Solutions</span></span>
  </div>

  <!-- CD label -->
  <div class="brand" style="left:874px; top:1392px; font-size:11px;">
    <span class="brand__dot"></span>
    <span class="brand__text"><span class="brand__name">Meadowline Ledger</span><span class="brand__tag">Accounting &amp; Tax Solutions</span></span>
  </div>

  <!-- CD sleeve -->
  <div class="brand" style="left:1155px; top:1303px; font-size:12px;">
    <span class="brand__dot"></span>
    <span class="brand__text"><span class="brand__name">Meadowline Ledger</span><span class="brand__tag">Accounting &amp; Tax Solutions</span></span>
  </div>
  <div class="contact contact--compact" style="left:1155px; top:1402px;">
    <span>555-214-0187</span><span>info@meadowlineledger.com</span><span>www.meadowlineledger.com</span><br><span>42 Fernbrook Rd, Marlow, Ohio, 43015</span>
  </div>

</div>
</body>
</html>
```